Harbor Lanterns Book Cover Design featuring a Phoenix and Flames

Please design the front cover of a book called Harbor Lanterns
By YOU!
Quiet Orchard Series
Book dimensions: 2150 x 1400mm
I am really open to design styles. I would like it to be powerful with a Phoenix and fire or even a woman's form. I may have gold leaf embossed on the cover if gold is used on the wings.
I have uploaded the logo should you wish to add this. Let me know if you have any questions.
Black as a colour is great too.
- Phoenix

```html
<!DOCTYPE html>
<html lang="en">
<head>
<meta charset="utf-8">
<title>Harbor Lanterns — Book Cover</title>
<link rel="stylesheet" href="https://fonts.googleapis.com/css2?family=Cinzel:wght@400;600;700&display=swap">
<style>
  :root {
    --ink: #0a0a0b;
    --rock: #262628;
    --rock-light: #55555a;
    --ember: #d4621a;
    --flame: #ff9a2e;
    --flame-hot: #ffe0a0;
    --brand: #e0561c;
    --rule: #5e5e62;
  }
  html, body {
    margin: 0;
    padding: 0;
    width: 781px;
    height: 1200px;
    overflow: hidden;
    background: var(--ink);
  }
  .cover {
    position: relative;
    width: 781px;
    height: 1200px;
    overflow: hidden;
    background: var(--ink);
    font-family: "Cinzel", serif;
  }
  .cover-artwork {
    position: absolute;
    inset: 0;
    background:
      radial-gradient(ellipse 9% 30% at 40% 40%, rgba(255,210,122,0.95) 0%, rgba(255,154,46,0.8) 45%, rgba(232,116,26,0) 100%),
      radial-gradient(ellipse 16% 38% at 40% 45%, rgba(240,110,25,0.85) 0%, rgba(200,70,10,0.4) 60%, rgba(200,70,10,0) 100%),
      radial-gradient(ellipse 40% 16% at 28% 72%, rgba(255,190,80,0.95) 0%, rgba(240,100,20,0.75) 45%, rgba(180,50,10,0) 100%),
      radial-gradient(ellipse 30% 10% at 75% 60%, rgba(230,90,20,0.55) 0%, rgba(230,90,20,0) 100%),
      radial-gradient(ellipse 45% 30% at 12% 20%, rgba(120,120,125,0.6) 0%, rgba(120,120,125,0) 100%),
      radial-gradient(ellipse 40% 30% at 90% 30%, rgba(110,110,115,0.5) 0%, rgba(110,110,115,0) 100%),
      linear-gradient(180deg, var(--rock-light) 0%, var(--rock) 50%, #151516 78%, var(--ink) 100%);
  }
  .series-mark {
    position: absolute;
    top: 44px;
    left: 560px;
    width: 184px;
    display: flex;
    flex-direction: column;
    align-items: center;
    gap: 12px;
  }
  .series-mark-dot {
    width: 40px;
    height: 40px;
    border-radius: 50%;
    background: var(--brand);
  }
  .series-mark-name {
    font-weight: 600;
    font-size: 13px;
    letter-spacing: 1.5px;
    color: var(--brand);
    white-space: nowrap;
  }
  .title-block {
    position: absolute;
    left: 0;
    right: 0;
    top: 975px;
    text-align: center;
  }
  .book-title {
    margin: 0;
    font-weight: 400;
    font-size: 132px;
    line-height: 1;
    letter-spacing: 10px;
    background: linear-gradient(180deg, var(--flame-hot) 0%, var(--flame) 40%, var(--ember) 100%);
    -webkit-background-clip: text;
    background-clip: text;
    color: transparent;
  }
  .book-subtitle {
    margin: 4px 0 0;
    font-weight: 400;
    font-size: 32px;
    line-height: 1;
    letter-spacing: 6px;
    color: var(--ember);
  }
  .title-rules {
    display: block;
    margin: 14px auto 0;
  }
</style>
</head>
<body>
  <main class="cover">
    <div class="cover-artwork" role="img" aria-label="A woman's figure formed of flames rising from a blaze among dark jagged rocks, sparks drifting upward"></div>

    <div class="series-mark">
      <span class="series-mark-dot"></span>
      <span class="series-mark-name">QUIET ORCHARD SERIES</span>
    </div>

    <header class="title-block">
      <h1 class="book-title">HARBOR</h1>
      <p class="book-subtitle">LANTERNS</p>
      <svg class="title-rules" width="625" height="4" viewBox="0 0 625 4" aria-hidden="true">
        <line x1="0" y1="2" x2="288" y2="2" stroke="var(--rule)" stroke-width="2"/>
        <line x1="337" y1="2" x2="625" y2="2" stroke="var(--rule)" stroke-width="2"/>
      </svg>
    </header>
  </main>
</body>
</html>
```